Velmont Recycling needs a new web design

We need a new web design for our company based in Austin, TX. We resell and recycling electronics such as laptops, computer components, Zelvos, Quorbs, etc. Since our inception over ten years ago, we’ve become one of the premier electronics recycling and remarketing companies in Austin, Texas.

```html
<!DOCTYPE html>
<html lang="en">
<head>
<meta charset="utf-8">
<title>Velmont Recycling</title>
<link href="https://fonts.googleapis.com/css2?family=Raleway:wght@400;500;600&display=swap" rel="stylesheet">
<style>
  :root {
    --blue: #2f7fe0;
    --ink: #333333;
    --muted: #8a8a8a;
    --band: #f2f2f2;
    --card: #ffffff;
    --coral: #f0566a;
    --warm-a: #fe5a69;
    --warm-b: #ff9a68;
    --cool-a: #3b8fe0;
    --cool-b: #58c8f0;
    --field: #f2a3a8;
    --map-a: #e4e4e0;
    --map-b: #d3d6cf;
  }
  * { box-sizing: border-box; margin: 0; padding: 0; }
  html, body { width: 859px; height: 1200px; overflow: hidden; }
  body { position: relative; background: #fff; font-family: "Raleway", sans-serif; color: var(--ink); }
  .abs { position: absolute; }
  .section-title { left: 0; width: 859px; text-align: center; font-weight: 400; font-size: 28px; color: var(--ink); }
  .section-title .accent, .accent-title { color: var(--blue); }
  .section-sub { left: 0; width: 859px; text-align: center; font-size: 12px; color: var(--muted); }

  .clients { top: 0; left: 0; width: 859px; height: 253px; }
  .clients-intro { top: 106px; left: 0; width: 859px; text-align: center; font-size: 12px; color: var(--ink); }
  .client-logo { top: 174px; font-size: 18px; font-weight: 600; color: #555; text-align: center; width: 110px; }
  .client-logo.boxed { top: 137px; height: 98px; width: 104px; left: 376px; background: #f3f3f3; line-height: 98px; }
  .client-dot { display: inline-block; width: 9px; height: 9px; border-radius: 50%; background: #555; margin-right: 5px; vertical-align: middle; }

  .milestones { top: 253px; left: 0; width: 859px; height: 251px; background: var(--band); }
  .stat-card { top: 123px; width: 115px; height: 86px; background: var(--card); box-shadow: 0 1px 4px rgba(0,0,0,.12); text-align: center; }
  .stat-label { margin-top: 16px; font-size: 10px; color: var(--ink); }
  .stat-value { margin-top: 10px; font-size: 25px; color: var(--blue); }

  .location { top: 504px; left: 0; width: 859px; height: 351px; }
  .map { top: 113px; left: 174px; width: 509px; height: 189px; background: linear-gradient(135deg, var(--map-a), var(--map-b)); box-shadow: 0 1px 4px rgba(0,0,0,.2); }

  .contact { top: 855px; left: 0; width: 859px; height: 323px; background: linear-gradient(90deg, var(--warm-a), var(--warm-b)); color: #fff; }
  .contact-title { top: 36px; left: 106px; font-size: 26px; font-weight: 400; }
  .contact-text { top: 80px; left: 106px; width: 360px; font-size: 11px; line-height: 1.55; }
  .info-label { font-size: 11px; font-weight: 600; display: flex; align-items: center; gap: 9px; }
  .info-value { font-size: 9.5px; margin-top: 8px; opacity: .95; }

  .form-card { top: 28px; left: 482px; width: 269px; height: 267px; background: #fff; box-shadow: 0 2px 8px rgba(0,0,0,.15); }
  .form-title { top: 14px; left: 0; width: 269px; text-align: center; font-size: 19px; color: var(--coral); font-weight: 400; }
  .field { border: 1px solid var(--field); height: 22px; font-size: 8px; color: #c9a0a4; padding: 6px 6px; }
  .submit { top: 224px; left: 101px; width: 67px; height: 23px; background: linear-gradient(90deg, var(--warm-a), var(--warm-b)); color: #fff; font-size: 10px; text-align: center; line-height: 23px; }

  .footer { top: 1178px; left: 0; width: 859px; height: 22px; background: linear-gradient(90deg, var(--cool-a), var(--cool-b)); color: #fff; }
  .footer-copy { top: 6px; left: 106px; font-size: 8px; }
  .social { top: 5px; left: 627px; display: flex; gap: 5px; }
  .social span { width: 11px; height: 11px; border-radius: 50%; background: #1f3f73; }
</style>
</head>
<body>

<section class="abs clients">
  <h2 class="abs section-title" style="top:38px">Our <span class="accent">Clients</span></h2>
  <p class="abs section-sub" style="top:76px">You got it right. They trust us.</p>
  <p class="abs clients-intro">We value our customers requirements and opinions. Together we make this earth a better place to live on.</p>
  <div class="abs client-logo" style="left:101px">Pellaro</div>
  <div class="abs client-logo" style="left:238px">Kestrane</div>
  <div class="abs client-logo boxed">Dorvane</div>
  <div class="abs client-logo" style="left:512px"><span class="client-dot"></span>Alteris</div>
  <div class="abs client-logo" style="left:648px">Quenby Bank</div>
</section>

<section class="abs milestones">
  <h2 class="abs section-title accent-title" style="top:36px">Milestones</h2>
  <p class="abs section-sub" style="top:74px">Prepare to be amazed</p>
  <div class="abs stat-card" style="left:161px"><p class="stat-label">Laptops Recycled</p><p class="stat-value">108690</p></div>
  <div class="abs stat-card" style="left:301px"><p class="stat-label">Mobiles Recycled</p><p class="stat-value">78350</p></div>
  <div class="abs stat-card" style="left:441px"><p class="stat-label">Home Appliances</p><p class="stat-value">180460</p></div>
  <div class="abs stat-card" style="left:583px"><p class="stat-label">KG E-Waste Recycled</p><p class="stat-value">8235700</p></div>
</section>

<section class="abs location">
  <h2 class="abs section-title accent-title" style="top:38px">Location</h2>
  <div class="abs map" role="img" aria-label="Street map of north Austin showing the Velmont Recycling location pin"></div>
</section>

<section class="abs contact">
  <h2 class="abs contact-title">Contact Us</h2>
  <p class="abs contact-text">Interested in helping to make the world a greener place?<br>Get in touch with Velmont Recycling, and learn more about the wide range of recycling services and facilities that are at your disposal.</p>

  <div class="abs" style="top:170px;left:106px">
    <p class="info-label">
      <svg width="9" height="12" viewBox="0 0 9 12"><path d="M4.5 0A4.5 4.5 0 0 0 0 4.5C0 8 4.5 12 4.5 12S9 8 9 4.5A4.5 4.5 0 0 0 4.5 0zm0 6.3a1.8 1.8 0 1 1 0-3.6 1.8 1.8 0 0 1 0 3.6z" fill="#fff"/></svg>
      Address
    </p>
    <p class="info-value">4120 Marlow Ridge Rd Austin TX USA 78745</p>
  </div>
  <div class="abs" style="top:224px;left:106px">
    <p class="info-label">
      <svg width="11" height="11" viewBox="0 0 24 24"><path d="M6.6 10.8a15.1 15.1 0 0 0 6.6 6.6l2.2-2.2a1 1 0 0 1 1-.25 11.4 11.4 0 0 0 3.6.57 1 1 0 0 1 1 1V20a1 1 0 0 1-1 1A17 17 0 0 1 3 4a1 1 0 0 1 1-1h3.5a1 1 0 0 1 1 1c0 1.25.2 2.45.57 3.6a1 1 0 0 1-.25 1z" fill="#fff"/></svg>
      Phone
    </p>
    <p class="info-value">(512) 555-0148</p>
  </div>
  <div class="abs" style="top:224px;left:201px">
    <p class="info-label">
      <svg width="12" height="9" viewBox="0 0 12 9"><rect width="12" height="9" rx="1" fill="#fff"/><path d="M0.5 0.8 6 5l5.5-4.2" stroke="#fe6f68" stroke-width="1" fill="none"/></svg>
      Email
    </p>
    <p class="info-value">hello@velmontrecycling.com</p>
  </div>

  <form class="abs form-card">
    <h3 class="abs form-title">Ask Us Anything!</h3>
    <div class="abs field" style="top:51px;left:16px;width:237px">Name</div>
    <div class="abs field" style="top:82px;left:16px;width:113px">Email</div>
    <div class="abs field" style="top:82px;left:140px;width:113px">Phone</div>
    <div class="abs field" style="top:114px;left:16px;width:237px">Subject</div>
    <div class="abs field" style="top:146px;left:16px;width:237px;height:64px">Message</div>
    <div class="abs submit">Submit</div>
  </form>
</section>

<footer class="abs footer">
  <p class="abs footer-copy">Copyright © Velmont Recycling</p>
  <div class="abs social"><span></span><span></span><span></span><span></span><span></span><span></span><span></span><span></span></div>
</footer>

</body>
</html>
```